Morvell Electric Business Card

An electrical contractor needs a business card design, that will stand out.
I would like designs that use the colors in the logo shown. The logo attached I am ok with but if you have a better idea I am open for suggestions. I like the color scheme.
Industry/Entity Type
Electrical
Contact Information for Business Card
Services, social media, QR code,

```html
<!DOCTYPE html>
<html lang="en">
<head>
<meta charset="utf-8">
<title>Morvell Electric Business Card</title>
<link href="https://fonts.googleapis.com/css2?family=Oswald:wght@500&family=Lato:wght@400&family=Montserrat:wght@700&display=swap" rel="stylesheet">
<style>
  :root {
    --backdrop: #e8e8e8;
    --card: #000000;
    --accent: #f0b921;
    --ink-light: #ffffff;
  }
  html, body {
    margin: 0;
    padding: 0;
    width: 1200px;
    height: 1200px;
    overflow: hidden;
    background: var(--backdrop);
  }
  .canvas {
    position: relative;
    width: 1200px;
    height: 1200px;
  }
  .card {
    position: absolute;
    background: var(--card);
    border-radius: 25px;
    box-shadow: 0 4px 14px rgba(0,0,0,0.35);
  }
  .card--front { left: 188px; top: 91px; width: 823px; height: 474px; }
  .card--back  { left: 186px; top: 635px; width: 828px; height: 474px; }

  .front-brand {
    position: absolute;
    right: 27px;
    top: 24px;
    display: flex;
    flex-direction: column;
    align-items: flex-end;
    gap: 10px;
  }
  .front-brand__square {
    width: 54px;
    height: 54px;
    background: var(--accent);
  }
  .front-brand__name {
    font-family: 'Montserrat', sans-serif;
    font-weight: 700;
    font-size: 14px;
    letter-spacing: 0.5px;
    color: var(--ink-light);
  }

  .person {
    position: absolute;
    right: 450px;
    top: 188px;
    text-align: right;
  }
  .person__name {
    font-family: 'Oswald', sans-serif;
    font-weight: 500;
    font-size: 54px;
    line-height: 1;
    color: var(--accent);
    letter-spacing: 0.3px;
  }
  .person__role {
    font-family: 'Lato', sans-serif;
    font-size: 21px;
    color: var(--ink-light);
    margin-top: 6px;
  }
  .divider {
    position: absolute;
    left: 410px;
    top: 198px;
    width: 3px;
    height: 78px;
    background: var(--accent);
  }
  .contact {
    position: absolute;
    left: 446px;
    top: 193px;
    list-style: none;
    margin: 0;
    padding: 0;
  }
  .contact__item {
    display: flex;
    align-items: center;
    height: 30px;
    font-family: 'Lato', sans-serif;
    font-size: 20px;
    color: var(--ink-light);
  }
  .contact__icon {
    width: 20px;
    height: 20px;
    margin-right: 12px;
    flex: none;
  }

  .back-brand {
    position: absolute;
    left: 0;
    right: 0;
    top: 110px;
    display: flex;
    flex-direction: column;
    align-items: center;
    gap: 42px;
  }
  .back-brand__square {
    width: 170px;
    height: 170px;
    background: var(--accent);
  }
  .back-brand__name {
    font-family: 'Montserrat', sans-serif;
    font-weight: 700;
    font-size: 51px;
    line-height: 1;
    color: var(--ink-light);
    letter-spacing: 0.5px;
  }
</style>
</head>
<body>
<div class="canvas">

  <section class="card card--front">
    <div class="front-brand">
      <div class="front-brand__square"></div>
      <div class="front-brand__name">MORVELL ELECTRIC</div>
    </div>

    <div class="person">
      <div class="person__name">DARREN HOLT</div>
      <div class="person__role">CEO</div>
    </div>

    <div class="divider"></div>

    <ul class="contact">
      <li class="contact__item">
        <svg class="contact__icon" viewBox="0 0 24 24"><path fill="#f0b921" d="M6.6 10.8a15.1 15.1 0 0 0 6.6 6.6l2.2-2.2c.3-.3.7-.4 1-.2 1.1.4 2.3.6 3.6.6.6 0 1 .4 1 1V20c0 .6-.4 1-1 1A17 17 0 0 1 3 4c0-.6.4-1 1-1h3.5c.6 0 1 .4 1 1 0 1.3.2 2.5.6 3.6.1.3 0 .7-.2 1z"/></svg>
        000-123-456-789
      </li>
      <li class="contact__item">
        <svg class="contact__icon" viewBox="0 0 24 24"><rect x="2" y="5" width="20" height="14" fill="#f0b921"/><path d="M2 5l10 8 10-8M2 19l8-7M22 19l-8-7" stroke="#000" stroke-width="1.6" fill="none"/></svg>
        info@yourwebsitename.com
      </li>
      <li class="contact__item">
        <svg class="contact__icon" viewBox="0 0 24 24" fill="none" stroke="#f0b921" stroke-width="1.8"><circle cx="12" cy="12" r="10"/><ellipse cx="12" cy="12" rx="4.5" ry="10"/><path d="M2 12h20M4 7h16M4 17h16"/></svg>
        www.yourwebsitename.com
      </li>
    </ul>
  </section>

  <section class="card card--back">
    <div class="back-brand">
      <div class="back-brand__square"></div>
      <div class="back-brand__name">MORVELL ELECTRIC</div>
    </div>
  </section>

</div>
</body>
</html>
```